Brightway Rug and Floor cleaning Business card Design

I need a design that has the same feel as my van.
i would also like a prominent "Review us on facebook" somewhere, but not that it makes it look silly.
I would like the card to have a little bit of grey or black in the design as well.

It will need contact details
phone: 0498 276154
email: rkbrightwayfloors@mailbox-example.com
website: www.brightwayrugandfloorcleaning-example.com.au
facebook: /brightwayrugandfloorcleaning

Industry/Entity Type

Business

Contact Information for Business Card

Phone number 0498276154
Email rkbrightwayfloors@mailbox-example.com
Website www.brightwayrugandfloorcleaning-example.com.au
Facebook/brightwayrugandfloorcleaning

Colors
000000

Requirements
Must have
• Same feel as my van
• I want the card to stand out from the crowd
Nice to have
• Maybe include a tiny bit of a third colour? Grey's,blacks, orange?

```html
<!DOCTYPE html>
<html lang="en">
<head>
<meta charset="utf-8">
<title>Brightway Rug and Floor Cleaning – Business Card</title>
<link rel="stylesheet" href="https://fonts.googleapis.com/css2?family=Roboto:wght@400;700&family=Saira:wght@600;700&display=swap">
<style>
  :root {
    --stage: #3b3b3b;
    --card-white: #ffffff;
    --card-dark: #1a1c1d;
    --card-dark-band: #4a4c4e;
    --brand-blue: #1cb0da;
    --brand-green: #8cc63f;
    --text-grey: #555759;
    --rule-grey: #bdbdbd;
    --text-light: #e9ecee;
  }
  * { box-sizing: border-box; margin: 0; padding: 0; }
  html, body { width: 1105px; height: 1200px; overflow: hidden; }
  body { background: var(--stage); position: relative; font-family: "Roboto", Arial, sans-serif; }

  .card {
    position: absolute; left: 196px; width: 719px; height: 410px;
    box-shadow: 0 6px 18px rgba(0,0,0,.45); overflow: hidden;
  }
  .card--front { top: 146px; background: var(--card-white); }
  .card--back { top: 602px; background: var(--card-dark); }

  .brand {
    position: absolute; left: 0; right: 0; display: flex;
    align-items: center; justify-content: center; gap: 14px;
    font-family: "Saira", "Arial Narrow", sans-serif; font-weight: 700;
    font-size: 58px; line-height: 1; color: var(--brand-blue); letter-spacing: -0.5px;
  }
  .brand__dot { width: 26px; height: 26px; border-radius: 50%; background: var(--brand-blue); }
  .card--front .brand { top: 128px; }
  .card--back .brand { top: 168px; }

  .owner { position: absolute; right: 396px; top: 287px; text-align: right; line-height: 1.15; }
  .owner__name { font-weight: 700; font-size: 25px; color: var(--brand-blue); letter-spacing: .3px; }
  .owner__role { font-size: 19px; color: var(--brand-green); margin-top: 6px; letter-spacing: .3px; }
  .divider { position: absolute; left: 337px; top: 273px; width: 1px; height: 88px; background: var(--rule-grey); }

  .contacts { position: absolute; left: 362px; top: 273px; list-style: none; }
  .contacts li { display: flex; align-items: center; gap: 12px; height: 28px; font-size: 16px; color: var(--text-grey); }
  .contacts svg { width: 18px; height: 18px; fill: var(--brand-blue); flex: none; }
  .contacts .square { width: 16px; height: 16px; margin: 0 1px; background: var(--brand-blue); flex: none; }

  .back-texture {
    position: absolute; inset: 0;
    background: linear-gradient(110deg, var(--card-dark) 0%, #23272a 55%, var(--card-dark-band) 62%, #2d2f31 80%, #242628 100%);
  }
  .website {
    position: absolute; left: 0; right: 0; top: 294px; text-align: center;
    font-size: 18px; color: var(--text-light); letter-spacing: .4px;
  }
  .review {
    position: absolute; left: 0; right: 0; top: 336px; display: flex;
    justify-content: center; align-items: center; gap: 16px;
    font-family: "Saira", "Arial Narrow", sans-serif; font-weight: 700;
    font-size: 31px; line-height: 1.15; color: var(--brand-blue);
  }
  .review__square { width: 27px; height: 27px; background: var(--brand-green); }
</style>
</head>
<body>
  <section class="card card--front">
    <div class="brand"><span class="brand__dot"></span>Brightway</div>
    <div class="owner">
      <p class="owner__name">RYAN KESSLER</p>
      <p class="owner__role">OWNER/OPERATOR</p>
    </div>
    <div class="divider"></div>
    <ul class="contacts">
      <li>
        <svg viewBox="0 0 24 24" aria-hidden="true"><path d="M6.6 10.8a15.1 15.1 0 0 0 6.6 6.6l2.2-2.2c.3-.3.7-.4 1-.2 1.1.4 2.3.6 3.6.6.6 0 1 .4 1 1V20c0 .6-.4 1-1 1C10.6 21 3 13.4 3 4c0-.6.4-1 1-1h3.5c.6 0 1 .4 1 1 0 1.3.2 2.5.6 3.6.1.3 0 .7-.2 1z"/></svg>
        0498276154
      </li>
      <li>
        <svg viewBox="0 0 24 24" aria-hidden="true"><path d="M2 5h20v14H2z"/><path d="M3.5 6.5 12 12.5l8.5-6" fill="none" stroke="#fff" stroke-width="1.6"/></svg>
        rkbrightwayfloors@mailbox-example.com
      </li>
      <li><span class="square"></span>brightwayrugandfloorcleaning</li>
    </ul>
  </section>

  <section class="card card--back">
    <div class="back-texture" role="img" aria-label="Dark background scattered with soft translucent bubbles and a lighter diagonal sheen"></div>
    <div class="brand"><span class="brand__dot"></span>Brightway</div>
    <p class="website">WWW.BRIGHTWAYRUGANDFLOORCLEANING-EXAMPLE.COM.AU</p>
    <p class="review">REVIEW US ON <span class="review__square"></span></p>
  </section>
</body>
</html>
```